Sauce business needs a logo design and label design - Re-launching soon

Business based in Chicago, IL. We need a logo design (for Mabel's Sauces) and a label design for our Sauce product line. We make BBQ Sauces, Marinades, Salad dressings, Burger Sauces, Hot sauces, Ketchup, and Mustards
Our products are named under one brand: Mabel's Sauces... Each product will have a different name starting with Mabel's (depending on the flavor of the product). We are looking for a label that will catch consumers eye walking through the store. Our current label doesn't pop enough. We like the colors of Yellow, Red, Orange with a white or black background or any combination thereof.
* Will have to create a label that can be changed to fit particular sauce name and ingredient list, bar codes, etc
Please research designs as we do not want clipart or anything close to any other brands

Target Market(s)

Gourmet foodies, casual consumers,

Industry/Entity Type

Retail

Logo Text

Mabel's Sauces

Requirements
Must have
• Consistent brand scheme that works for all of my Sauce varieties
Should not have
• Clipart or designs/color schemes from other products/brands

```html
<!DOCTYPE html>
<html lang="en">
<head>
<meta charset="utf-8">
<title>Mabel's Sauces – Brand and Labels</title>
<link rel="stylesheet" href="https://fonts.googleapis.com/css2?family=Libre+Caslon+Text:wght@400;700&family=Kaushan+Script&family=Oswald:wght@300&family=Open+Sans:wght@400&display=swap">
<style>
  :root {
    --paper: #ffffff;
    --ink: #1e1e1e;
    --label-black: #2a2a2b;
    --label-grey: #4a4a4c;
    --cream: #f1efea;
    --sage: #8a9a7b;
    --sage-band: #93a184;
    --berry: #b33a4a;
    --berry-band: #b84a5a;
    --leaf: #7d8f6e;
    --rule: #9a9a9a;
  }
  * { box-sizing: border-box; margin: 0; padding: 0; }
  html, body { width: 1200px; height: 1200px; overflow: hidden; background: var(--paper); }
  .canvas { position: relative; width: 1200px; height: 1200px; background: var(--paper); }

  .brand-name {
    position: absolute; left: 119px; top: 212px; width: 340px;
    font-family: "Libre Caslon Text", Georgia, serif; font-weight: 700;
    font-size: 62px; line-height: 1.1; color: var(--ink); letter-spacing: 2px;
  }

  .label {
    position: absolute; width: 305px; height: 496px;
    background: linear-gradient(90deg, var(--label-black) 0%, var(--label-grey) 45%, var(--label-black) 100%);
    color: var(--cream); text-align: center; overflow: hidden;
  }
  .label--everyday { left: 451px; top: 566px; }
  .label--island { left: 823px; top: 560px; }

  .label__brand {
    margin-top: 46px;
    font-family: "Libre Caslon Text", Georgia, serif; font-weight: 400;
    font-size: 34px; line-height: 1.1; letter-spacing: 1px; color: var(--cream);
  }
  .label__flavor {
    margin-top: 22px;
    font-family: "Libre Caslon Text", Georgia, serif; font-weight: 700;
    font-size: 40px; line-height: 1; white-space: nowrap;
  }
  .label--everyday .label__flavor { color: var(--sage); }
  .label--island .label__flavor { color: var(--berry); font-size: 36px; }

  .label__claim {
    margin-top: 30px;
    font-family: "Libre Caslon Text", Georgia, serif; font-size: 18px; letter-spacing: 3px;
  }
  .label__leaf {
    display: block; margin: 8px auto 0; width: 40px; height: 30px;
    background: var(--leaf); border-radius: 50% 50% 40% 40%;
  }
  .label__free {
    display: flex; align-items: center; justify-content: center; gap: 10px;
    margin-top: 8px; font-family: "Kaushan Script", cursive; font-size: 17px;
  }
  .label__free::before, .label__free::after {
    content: ""; width: 60px; border-top: 1px dashed var(--cream);
  }
  .label__free-list {
    margin: 12px auto 0; width: 200px; border: 1px solid var(--rule);
    font-family: "Oswald", sans-serif; font-weight: 300; font-size: 13px; letter-spacing: 1px;
  }
  .label__free-list span { display: block; padding: 3px 0; }
  .label__free-list span + span { border-top: 1px solid var(--rule); }
  .label__weight-title {
    margin-top: 6px; font-family: "Kaushan Script", cursive; font-size: 14px;
  }
  .label__rule {
    position: absolute; left: 0; right: 0; top: 443px; border-top: 2px solid var(--cream);
  }
  .label__band { position: absolute; left: 0; right: 0; bottom: 0; height: 42px; }
  .label--everyday .label__band { background: var(--sage-band); }
  .label--island .label__band { background: var(--berry-band); }
  .label__weight {
    position: absolute; left: 50%; top: 436px; transform: translateX(-50%);
    background: #fff; color: #333; border: 1px solid #777;
    font-family: "Open Sans", sans-serif; font-size: 13px; padding: 2px 8px; white-space: nowrap;
  }
</style>
</head>
<body>
<main class="canvas">
  <div class="brand-name">MABEL'S<br>SAUCES</div>

  <section class="label label--everyday">
    <div class="label__brand">MABEL'S<br>SAUCES</div>
    <div class="label__flavor">EVERYDAY</div>
    <div class="label__claim">ALL NATURAL</div>
    <span class="label__leaf" role="img" aria-label="Small leaf emblem"></span>
    <div class="label__free">Free of</div>
    <div class="label__free-list">
      <span>GLUTEN &nbsp;|&nbsp; GMO &nbsp;|&nbsp; ADDITIVES</span>
      <span>PRESERVATIVES &nbsp;|&nbsp; COLORING</span>
    </div>
    <div class="label__weight-title">Net Weight</div>
    <div class="label__rule"></div>
    <div class="label__band"></div>
    <div class="label__weight">12 oz (355ml)</div>
  </section>

  <section class="label label--island">
    <div class="label__brand">MABEL'S<br>SAUCES</div>
    <div class="label__flavor">ISLAND BBQ</div>
    <div class="label__claim">ALL NATURAL</div>
    <span class="label__leaf" role="img" aria-label="Small leaf emblem"></span>
    <div class="label__free">Free of</div>
    <div class="label__free-list">
      <span>GLUTEN &nbsp;|&nbsp; GMO &nbsp;|&nbsp; ADDITIVES</span>
      <span>PRESERVATIVES &nbsp;|&nbsp; COLORING</span>
    </div>
    <div class="label__weight-title">Net Weight</div>
    <div class="label__rule"></div>
    <div class="label__band"></div>
    <div class="label__weight">12 oz (355ml)</div>
  </section>
</main>
</body>
</html>
```